Erstellung einer ersten Einladungskarte „Safe the Date“
Zielgruppe
Spezialist für temporäres Linienmanagement & Projektmanagement
Als Sozietät für professionelles Interim Management bündelt die brückwerk AG die fachliche Kompetenz und die langjährige Erfahrung erfolgreicher Führungspersönlichkeiten aus nahezu allen Sektoren der Wirtschaft. Wir unterstützen unsere Kunden bei der Bewältigung temporärer Herausforderungen im Linienmanagement sowie im Management komplexer strategischer Projekte und Programme.
https://www.brueckwerk-example.net/de/home.html
Aufgabenstellung
Siehe angehängtes Briefing und angehängtes CD Manual, das nicht zwingend eingehalten werden muss für diesen Job

```html
<!DOCTYPE html>
<html lang="de">
<head>
<meta charset="utf-8">
<title>brückwerk AG – Save the Date</title>
<link rel="stylesheet" href="https://fonts.googleapis.com/css2?family=Titillium+Web:wght@400;600&display=swap">
<style>
  :root {
    --slate: #426a82;
    --slate-light: #4d7690;
    --slate-dark: #3a6079;
    --orange: #f06a22;
    --white: #ffffff;
  }
  * { margin: 0; padding: 0; box-sizing: border-box; }
  html, body {
    width: 1200px;
    height: 571px;
    overflow: hidden;
    background: var(--slate);
  }
  .card {
    position: relative;
    width: 1200px;
    height: 571px;
    overflow: hidden;
    font-family: "Titillium Web", sans-serif;
  }
  .card__backdrop {
    position: absolute;
    inset: 0;
    background: linear-gradient(160deg, var(--slate-light) 0%, var(--slate) 50%, var(--slate-dark) 100%);
  }
  .card__band {
    position: absolute;
    left: 0;
    top: 239px;
    width: 1157px;
    height: 189px;
  }
  .band { fill: var(--orange); }

  .brand {
    position: absolute;
    left: 662px;
    top: 0;
    width: 494px;
    height: 162px;
    background: var(--white);
    display: flex;
    align-items: center;
    justify-content: center;
  }
  .brand__name {
    font-size: 76px;
    font-weight: 600;
    color: var(--slate);
    letter-spacing: 1px;
    line-height: 1;
  }

  .headline {
    position: absolute;
    left: 180px;
    top: 270px;
    font-size: 98px;
    font-weight: 400;
    color: var(--white);
    line-height: 1.2;
    letter-spacing: 1px;
    white-space: nowrap;
  }
</style>
</head>
<body>
  <main class="card">
    <div class="card__backdrop" role="img" aria-label="Dekoratives Muster aus sich überlagernden weißen und orangefarbenen Kreisringen auf blaugrauem Grund"></div>

    <svg class="card__band" viewBox="0 0 1157 189" aria-hidden="true">
      <polygon class="band" points="0,0 1157,0 1071,189 0,189"/>
    </svg>

    <div class="brand">
      <span class="brand__name">brückwerk</span>
    </div>

    <h1 class="headline">Safe the Date</h1>
  </main>
</body>
</html>
```